Online-Marketing Material für Alltagsbegleiter
Zielgruppe
Wir bieten Haushaltshilfen und Alltagsbegleiter für Privathaushalte an. Unsere Hauptkundenklientel sind Pflegebedürftige Menschen denen eine Haushaltshilfe von der Pflegekasse zusteht. Weitere Kunden sind Familien und/oder Singlehaushalte, die eine Haushaltfshilfe benötigen.
Aufgabenstellung
Es soll ein neues Titelbild für unsere Facebokseite erstellt werden. Das Titelbild soll unser Logo enthalten und ggfls. auch ein paar Schrftzüge, bzw. Texte von unserer Internetseite. Das Titelbild soll leicht, locker und modern rüber kommen.

```html
<!DOCTYPE html>
<html lang="es">
<head>
<meta charset="utf-8">
<title>Lindenhand – Seite</title>
<link rel="stylesheet" href="https://fonts.googleapis.com/css2?family=Cinzel:wght@500&family=PT+Sans:wght@400;700&family=Roboto:wght@400;500;700&display=swap">
<style>
  :root {
    --page-bg: #f0f2f5;
    --chrome-bg: #f6f6f6;
    --white: #ffffff;
    --ink: #050505;
    --ink-soft: #65676b;
    --line: #ced0d4;
    --btn-grey: #e4e6eb;
    --accent-blue: #0866ff;
    --link-blue: #216fdb;
    --open-green: #31a24c;
    --brand-red: #c8102e;
    --band-red: rgba(200, 16, 46, 0.9);
    --icon-grey: #65676b;
  }
  * { box-sizing: border-box; }
  html, body {
    margin: 0; padding: 0;
    width: 1200px; height: 889px;
    overflow: hidden;
    background: var(--page-bg);
    font-family: "Roboto", sans-serif;
    color: var(--ink);
  }
  .canvas { position: relative; width: 1200px; height: 889px; overflow: hidden; }
  .abs { position: absolute; }

  /* browser chrome */
  .browser-bar { left: 0; top: 0; width: 1200px; height: 45px; background: var(--chrome-bg); border-bottom: 1px solid #dcdcdc; }
  .light { top: 17px; width: 11px; height: 11px; border-radius: 50%; }
  .address { left: 357px; top: 11px; width: 485px; height: 23px; border: 1px solid #d6d6d6; border-radius: 6px; background: #fbfbfb; font-size: 12px; text-align: center; line-height: 21px; color: #222; }

  /* site nav */
  .site-nav { left: 0; top: 45px; width: 1200px; height: 41px; background: var(--white); box-shadow: 0 1px 2px rgba(0,0,0,0.12); }
  .site-name { left: 8px; top: 13px; font-size: 12px; font-weight: 700; color: var(--accent-blue); }
  .search { left: 76px; top: 7px; width: 177px; height: 27px; border-radius: 14px; background: var(--page-bg); font-size: 11px; color: var(--ink-soft); line-height: 27px; padding-left: 26px; }
  .search svg { position: absolute; left: 9px; top: 8px; }
  .nav-icon { top: 11px; }
  .round-btn { top: 6px; width: 29px; height: 29px; border-radius: 50%; background: var(--btn-grey); display: flex; align-items: center; justify-content: center; }
  .badge { left: 1141px; top: 2px; width: 13px; height: 13px; border-radius: 50%; background: #e41e3f; color: #fff; font-size: 8px; text-align: center; line-height: 13px; }
  .avatar-photo { left: 1159px; top: 6px; width: 29px; height: 29px; border-radius: 50%; background: linear-gradient(135deg, #5a3b2e, #c9a48a); }

  /* page header */
  .header-white { left: 0; top: 86px; width: 1200px; height: 471px; background: linear-gradient(180deg, #e9eaec 0%, #ffffff 60%); }
  .cover { left: 138px; top: 86px; width: 924px; height: 340px; overflow: hidden; }
  .cover-photo { position: absolute; inset: 0;
    background:
      radial-gradient(ellipse at 72% 40%, rgba(250, 200, 120, 0.55), transparent 35%),
      radial-gradient(ellipse at 28% 55%, rgba(255, 205, 90, 0.6), transparent 50%),
      linear-gradient(90deg, #b5650f 0%, #efa22c 25%, #e58f22 38%, #3a1c0a 41%, #2a1407 44%, #c9792a 52%, #6a3a16 70%, #2a1608 88%, #4a2a10 100%); }
  .cover svg { position: absolute; left: 0; top: 0; }
  .cover-headline { font-family: "PT Sans", sans-serif; font-size: 34px; fill: var(--white); }
  .service-list { font-family: "Cinzel", serif; font-weight: 500; font-size: 14px; fill: var(--white); }

  .brand-badge { left: 162px; top: 368px; width: 130px; height: 130px; border-radius: 50%; background: var(--white); box-shadow: 0 0 0 3px var(--white), 0 1px 3px rgba(0,0,0,0.2); display: flex; align-items: center; justify-content: center; }
  .brand-badge span { font-family: "PT Sans", sans-serif; font-weight: 700; font-size: 21px; color: var(--brand-red); }

  .page-title { left: 302px; top: 443px; font-size: 24px; font-weight: 700; }
  .page-stats { left: 302px; top: 474px; font-size: 11px; font-weight: 500; color: var(--ink-soft); }

  .action { top: 462px; height: 26px; border-radius: 4px; font-size: 11px; font-weight: 700; display: flex; align-items: center; justify-content: center; gap: 5px; background: var(--btn-grey); }
  .action.primary { background: var(--accent-blue); color: var(--white); }

  .rule { left: 162px; top: 512px; width: 874px; height: 1px; background: var(--line); }
  .tab { top: 527px; font-size: 11px; font-weight: 500; color: var(--ink-soft); }
  .tab.active { color: var(--accent-blue); }
  .tab-line { left: 162px; top: 554px; width: 98px; height: 3px; background: var(--accent-blue); }
  .more-btn { left: 1002px; top: 521px; width: 34px; height: 27px; border-radius: 4px; background: var(--btn-grey); text-align: center; font-weight: 700; font-size: 12px; line-height: 20px; }

  /* cards */
  .card { background: var(--white); border-radius: 6px; box-shadow: 0 1px 2px rgba(0,0,0,0.12); }
  .card-title { font-size: 14.5px; font-weight: 700; }
  .intro { left: 163px; top: 569px; width: 360px; height: 330px; }
  .intro .desc { position: absolute; left: 12px; top: 35px; width: 336px; text-align: center; font-size: 11px; line-height: 14px; }
  .intro .divider { position: absolute; left: 12px; top: 73px; width: 336px; height: 1px; background: var(--line); }
  .row { position: absolute; left: 12px; font-size: 11px; display: flex; align-items: center; gap: 9px; white-space: nowrap; }
  .row svg { flex: none; }
  .row .link { color: var(--link-blue); }
  .row .open { color: var(--open-green); }

  .posts-head { left: 535px; top: 569px; width: 501px; height: 38px; }
  .filter-btn { position: absolute; right: 11px; top: 6px; width: 67px; height: 25px; border-radius: 4px; background: var(--btn-grey); font-size: 11px; font-weight: 700; display: flex; align-items: center; justify-content: center; gap: 4px; }

  .post { left: 535px; top: 620px; width: 501px; height: 290px; overflow: hidden; }
  .post-avatar { position: absolute; left: 13px; top: 7px; width: 28px; height: 28px; border-radius: 50%; border: 2px solid var(--brand-red); background: var(--white); }
  .post-name { position: absolute; left: 48px; top: 8px; font-size: 11px; font-weight: 700; }
  .post-date { position: absolute; left: 48px; top: 23px; font-size: 9.5px; color: var(--ink-soft); }
  .post-dots { position: absolute; right: 14px; top: 5px; font-size: 13px; font-weight: 700; color: var(--ink-soft); }
  .post-text { position: absolute; left: 12px; top: 42px; width: 480px; font-size: 11px; line-height: 14px; }
  .post-text p { margin: 0 0 5px; }
  .post-photo { position: absolute; left: 0; top: 160px; width: 501px; height: 130px; background: linear-gradient(120deg, #e9ecef 0%, #cfd5da 45%, #b89a86 75%, #7d6458 100%); }

  .compose { left: 1153px; top: 843px; width: 34px; height: 34px; border-radius: 50%; background: var(--white); box-shadow: 0 1px 4px rgba(0,0,0,0.25); display: flex; align-items: center; justify-content: center; }
</style>
</head>
<body>
<main class="canvas">

  <header class="abs browser-bar">
    <span class="abs light" style="left:17px;background:#ff5f57"></span>
    <span class="abs light" style="left:35px;background:#febc2e"></span>
    <span class="abs light" style="left:52px;background:#28c840"></span>
    <div class="abs address">🔒 treffpunkt.com</div>
  </header>

  <nav class="abs site-nav">
    <span class="abs site-name">Treffpunkt</span>
    <div class="abs search">
      <svg width="11" height="11" viewBox="0 0 12 12"><circle cx="5" cy="5" r="4" fill="none" stroke="#65676b" stroke-width="1.5"/><path d="M8 8l3 3" stroke="#65676b" stroke-width="1.5"/></svg>
      Buscar en Treffpunkt
    </div>
    <svg class="abs nav-icon" style="left:387px" width="20" height="20" viewBox="0 0 20 20"><path d="M3 9l7-6 7 6v8H3z" fill="none" stroke="#65676b" stroke-width="1.6"/></svg>
    <svg class="abs nav-icon" style="left:488px" width="20" height="20" viewBox="0 0 20 20"><rect x="2" y="3" width="16" height="12" rx="3" fill="none" stroke="#65676b" stroke-width="1.6"/><path d="M8 6v6l5-3z" fill="#65676b"/><path d="M6 18h8" stroke="#65676b" stroke-width="1.6"/></svg>
    <svg class="abs nav-icon" style="left:589px" width="20" height="20" viewBox="0 0 20 20"><path d="M3 4h14l1 4H2zM4 8v9h12V8" fill="none" stroke="#65676b" stroke-width="1.6"/><rect x="8" y="12" width="4" height="5" fill="none" stroke="#65676b" stroke-width="1.4"/></svg>
    <svg class="abs nav-icon" style="left:691px" width="20" height="20" viewBox="0 0 20 20"><circle cx="10" cy="10" r="8" fill="none" stroke="#65676b" stroke-width="1.6"/><circle cx="10" cy="8" r="2.5" fill="none" stroke="#65676b" stroke-width="1.4"/><path d="M5 15c2-3 8-3 10 0" fill="none" stroke="#65676b" stroke-width="1.4"/></svg>
    <svg class="abs nav-icon" style="left:792px" width="20" height="20" viewBox="0 0 20 20"><rect x="2" y="5" width="16" height="10" rx="4" fill="none" stroke="#65676b" stroke-width="1.6"/><path d="M6 8v4M4 10h4" stroke="#65676b" stroke-width="1.4"/><circle cx="13" cy="10" r="1.2" fill="#65676b"/></svg>
    <div class="abs round-btn" style="left:1052px"><svg width="13" height="13" viewBox="0 0 13 13"><g fill="#050505"><rect x="0" y="0" width="3" height="3"/><rect x="5" y="0" width="3" height="3"/><rect x="10" y="0" width="3" height="3"/><rect x="0" y="5" width="3" height="3"/><rect x="5" y="5" width="3" height="3"/><rect x="10" y="5" width="3" height="3"/><rect x="0" y="10" width="3" height="3"/><rect x="5" y="10" width="3" height="3"/><rect x="10" y="10" width="3" height="3"/></g></svg></div>
    <div class="abs round-btn" style="left:1088px"><svg width="14" height="14" viewBox="0 0 14 14"><path d="M2 2h10v7H6l-3 3V9H2z" fill="#050505"/></svg></div>
    <div class="abs round-btn" style="left:1123px"><svg width="13" height="14" viewBox="0 0 13 14"><path d="M6.5 1c3 0 4.5 2 4.5 5v3l1.5 2H.5L2 9V6c0-3 1.5-5 4.5-5zM5 12h3a1.5 1.5 0 0 1-3 0z" fill="#050505"/></svg></div>
    <span class="abs badge">3</span>
    <div class="abs avatar-photo" role="img" aria-label="Profilfoto der angemeldeten Person"></div>
  </nav>

  <div class="abs header-white"></div>

  <section class="abs cover">
    <div class="cover-photo" role="img" aria-label="Foto: ältere Frau mit Brille, von hinten gesehen, blickt im warmen Abendlicht aus einem Fenster"></div>
    <svg width="924" height="340" viewBox="0 0 924 340" aria-label="Titelbild Text">
      <text class="cover-headline" x="83" y="160" textLength="265" lengthAdjust="spacingAndGlyphs">Wir sind für Sie da!</text>
      <defs>
        <linearGradient id="bandFade" x1="0" x2="1" y1="0" y2="0">
          <stop offset="0" stop-color="#c8102e" stop-opacity="0.15"/>
          <stop offset="0.2" stop-color="#c8102e" stop-opacity="0.9"/>
          <stop offset="1" stop-color="#c8102e" stop-opacity="0.9"/>
        </linearGradient>
      </defs>
      <rect x="0" y="303" width="924" height="37" fill="url(#bandFade)"/>
      <text class="service-list" x="162" y="327" textLength="750" lengthAdjust="spacingAndGlyphs">Haushaltshilfe · Einkaufsservice · Wäscheservice · Kehrwoche · Fensterreinigung · Alltagsbegleitung</text>
    </svg>
  </section>

  <div class="abs brand-badge"><span>Lindenhand</span></div>

  <h1 class="abs page-title" style="margin:0">Lindenhand</h1>
  <div class="abs page-stats">3 Me gusta · 2 seguidores</div>

  <div class="abs action primary" style="left:755px;width:115px">
    <svg width="11" height="11" viewBox="0 0 12 12"><circle cx="6" cy="6" r="5.5" fill="#fff"/></svg>Enviar mensaje
  </div>
  <div class="abs action" style="left:877px;width:82px">
    <svg width="12" height="11" viewBox="0 0 12 11"><path d="M0 5h2.5v6H0zM3.5 5L6 0c1.5 0 1.5 1.5 1.2 3H11c1 0 1 1 .8 1.5L10.5 10c-.2.6-.6 1-1.3 1H3.5z" fill="#050505"/></svg>Me gusta
  </div>
  <div class="abs action" style="left:966px;width:70px">
    <svg width="11" height="11" viewBox="0 0 12 12"><circle cx="5" cy="5" r="4" fill="none" stroke="#050505" stroke-width="1.6"/><path d="M8 8l3 3" stroke="#050505" stroke-width="1.6"/></svg>Buscar
  </div>

  <div class="abs rule"></div>
  <span class="abs tab active" style="left:174px">Publicaciones</span>
  <span class="abs tab" style="left:272px">Información</span>
  <span class="abs tab" style="left:361px">Menciones</span>
  <span class="abs tab" style="left:442px">Opiniones</span>
  <span class="abs tab" style="left:520px">Seguidores</span>
  <span class="abs tab" style="left:605px">Fotos</span>
  <span class="abs tab" style="left:658px">Ver más ▾</span>
  <div class="abs tab-line"></div>
  <div class="abs more-btn">···</div>

  <section class="abs card intro">
    <div class="abs card-title" style="left:12px;top:12px">Detalles</div>
    <div class="desc">Haushaltshilfen und Alltagsbegleiter für pflegebedürftige<br>Personen, Familien und Singlehaushalte</div>
    <div class="divider"></div>
    <div class="row" style="top:90px"><svg width="14" height="14" viewBox="0 0 14 14"><circle cx="7" cy="7" r="7" fill="#8a8d91"/><rect x="6.2" y="6" width="1.6" height="5" fill="#fff"/><circle cx="7" cy="4" r="1" fill="#fff"/></svg><span><b>Página</b> · Contratista · Servicio a domicilio</span></div>
    <div class="row" style="top:121px"><svg width="14" height="14" viewBox="0 0 14 14"><path d="M7 0l7 7-7 7-7-7z" fill="#8a8d91"/><path d="M5 9V6h4l-1.5-1.5M9 6l-1.5 1.5" stroke="#fff" stroke-width="1.2" fill="none"/></svg><span>Lindenweg 14, Musterstadt, Germany</span></div>
    <div class="row" style="top:152px"><svg width="14" height="14" viewBox="0 0 14 14"><path d="M3 1l2.5 3-1.5 1.5c1 2 2.5 3.5 4.5 4.5L10 8.5l3 2.5-1.5 2C6 13 1 8 1 2.5z" fill="#8a8d91"/></svg><span>0123 45678900</span></div>
    <div class="row" style="top:183px"><svg width="14" height="14" viewBox="0 0 14 14"><rect x="0" y="2" width="14" height="10" rx="1" fill="#8a8d91"/><path d="M1 3l6 5 6-5" stroke="#fff" stroke-width="1.2" fill="none"/></svg><span>kontakt@lindenhand.de</span></div>
    <div class="row" style="top:214px"><svg width="14" height="14" viewBox="0 0 14 14"><circle cx="7" cy="7" r="6.3" fill="none" stroke="#8a8d91" stroke-width="1.4"/><ellipse cx="7" cy="7" rx="2.6" ry="6.3" fill="none" stroke="#8a8d91" stroke-width="1.2"/><path d="M1 7h12" stroke="#8a8d91" stroke-width="1.2"/></svg><span class="link">lindenhand.de</span></div>
    <div class="row" style="top:245px"><svg width="14" height="14" viewBox="0 0 14 14"><circle cx="7" cy="7" r="7" fill="#8a8d91"/><path d="M7 3v4l3 2" stroke="#fff" stroke-width="1.3" fill="none"/></svg><span class="open">Siempre abierto</span><span style="color:#65676b">⌄</span></div>
    <div class="row" style="top:276px"><svg width="14" height="14" viewBox="0 0 14 14"><path d="M7 0l2.1 4.5 4.9.6-3.6 3.3 1 4.9L7 10.9 2.6 13.3l1-4.9L0 5.1l4.9-.6z" fill="#8a8d91"/></svg><span>Todavía sin calificar (0 opiniones)</span><svg width="14" height="14" viewBox="0 0 14 14"><circle cx="7" cy="7" r="7" fill="#65676b"/><rect x="6.2" y="6" width="1.6" height="5" fill="#fff"/><circle cx="7" cy="4" r="1" fill="#fff"/></svg></div>
  </section>

  <section class="abs card posts-head">
    <div class="abs card-title" style="left:12px;top:10px">Publicaciones</div>
    <div class="filter-btn"><svg width="12" height="10" viewBox="0 0 12 10"><path d="M0 2h12M0 8h12" stroke="#050505" stroke-width="1.2"/><circle cx="4" cy="2" r="1.6" fill="#fff" stroke="#050505"/><circle cx="8" cy="8" r="1.6" fill="#fff" stroke="#050505"/></svg>Filtros</div>
  </section>

  <article class="abs card post">
    <div class="post-avatar"></div>
    <div class="post-name">Lindenhand</div>
    <div class="post-date">23 de julio · 🌐</div>
    <div class="post-dots">···</div>
    <div class="post-text">
      <p>Wussten Sie schon? Pflegebedürftige in den Pflegegraden 1 bis 5 haben nach § 45b SGB XI Anspruch auf einen monatlichen Entlastungsbetrag von 125 Euro! Dieser Betrag hilft, den Alltag zu erleichtern und kann für haushaltsnahe Dienstleistungen wie Alltagsbegleitung und Haushaltshilfe genutzt werden. 🏠 🧹</p>
      <p>Die Abrechnung erfolgt direkt über den Dienstleister bei der Pflegekasse, Ihnen bleibt also der Abrechnungsaufwand erspart!</p>
      <p>Mehr Informationen erhalten Sie bei uns. Lassen Si... <b>Ver más</b></p>
    </div>
    <div class="post-photo" role="img" aria-label="Foto: Hände einer älteren Person in hellem Licht"></div>
  </article>

  <div class="abs compose"><svg width="15" height="15" viewBox="0 0 15 15"><path d="M7 2H2v11h11V8" fill="none" stroke="#050505" stroke-width="1.5"/><path d="M6 9l1-3 6-5 2 2-6 5z" fill="#050505"/></svg></div>

</main>
</body>
</html>
```